One page company profile for exclusive wine import

Valtrenor is an importer of exclusive, rare wines into indonesia. We would like a stylish, classy, upmarket but professional one pager containing our company profile.

Please include the text we prepared (see must haves) and read through it to get a better understanding of what our company is doing

We would like the one pager to have a dark background, and contain a drawing or drawing-style picture related to wine and/or global import (see examples). We would like to have it in PDF as well as in a word-template so we can later produce translations and/or adaptations to the text.

Target Market(s)

The one pagers is directed to distributors and upmarket hotels and restaurants.

Requirements
Must have
• We would like the one pager to have a dark background, and contain a drawing or drawing-style picture related to wine and/or global import (see examples)
• Our logo (see files) on the one pager
• The following contact details: E-mail: info@valtrenor-example.eu
• Word template and PDF
• The following text:
• "Valtrenor brings rare, exceptional wines to the Indonesian market. We
• specialize in French and Italian wines that even in Europe are very hard
• to get by. We have an extensive network of big and small, famous and less
• known winemakers that reserve a portion of their production for us.
• Together with them, we supply the market with an excellent range of the
• absolute best European wines.
• We buy our products directly at the winemaker in France or Italy Through a
• licensed importer, the wines are brought to Indonesia by airfreight and
• stored in air-conditioned, optimal conditions, awaiting distribution to
• our customers. All of this ensured that the wine loses none of its quality
• during transport from the winemaker to the customer.
• We always look out for partners that are eager to distribute or retail.
• Our intentions working with them are always to work on a long term basis.
• With these intentions we see that both sides together have to engage
• themselves to succeed in sales and establishing brand recognition in the
• Indonesian market. Our philosophy is based on trust, responsibility,
• mutual respect and of course a love for great wine!
• We advise our clients on tasting, food pairing, storing and aging the wine
• and provide a technical datasheet with all our bottles. We pride ourselves
• in our customer service and are always available for any enquiry."
Should not have
• clichés like pictures of grapes, vineyards, barrels, etc... (stylised drawings are preferred and allowed)

```html
<!DOCTYPE html>
<html lang="en">
<head>
<meta charset="utf-8">
<title>Valtrenor – Company Profile</title>
<link href="https://fonts.googleapis.com/css2?family=Montserrat:wght@300;400;600&display=swap" rel="stylesheet">
<style>
  :root {
    --wine-deep: #3a0608;
    --wine-mid: #6a1014;
    --wine-light: #7c1a1c;
    --band: #3e0c0e;
    --ink: #ffffff;
    --ink-soft: rgba(255,255,255,0.92);
    --rule: rgba(255,255,255,0.85);
    --mark-blue: #2b56a6;
  }
  html, body {
    margin: 0;
    padding: 0;
    width: 906px;
    height: 1200px;
    overflow: hidden;
    background: var(--wine-deep);
  }
  .page {
    position: relative;
    width: 906px;
    height: 1200px;
    overflow: hidden;
    font-family: "Montserrat", sans-serif;
    color: var(--ink);
    background:
      radial-gradient(ellipse at 55% 35%, var(--wine-light) 0%, var(--wine-mid) 40%, var(--wine-deep) 100%);
  }
  .profile-frame {
    position: absolute;
    left: 46px;
    top: -2px;
    width: 531px;
    height: 1005px;
    border: 1px solid var(--rule);
    box-sizing: border-box;
  }
  .brand {
    position: absolute;
    left: 48px;
    top: 40px;
    display: flex;
    align-items: center;
    gap: 20px;
  }
  .brand-dot {
    width: 78px;
    height: 78px;
    border-radius: 50%;
    background: var(--mark-blue);
  }
  .brand-name {
    font-weight: 600;
    font-size: 44px;
    letter-spacing: 2px;
    text-transform: uppercase;
    color: var(--ink);
  }
  .profile-text {
    position: absolute;
    left: 80px;
    top: 283px;
    width: 463px;
    margin: 0;
    font-weight: 300;
    font-size: 16.6px;
    line-height: 22.3px;
    text-align: justify;
    color: var(--ink-soft);
  }
  .glass-illustration {
    position: absolute;
    left: 619px;
    top: 159px;
    width: 287px;
    height: 866px;
  }
  .contact-band {
    position: absolute;
    left: 0;
    bottom: 0;
    width: 906px;
    height: 65px;
    background: var(--band);
    display: flex;
    align-items: center;
    justify-content: center;
  }
  .contact-email {
    font-weight: 400;
    font-size: 15px;
    letter-spacing: 6px;
    color: var(--ink);
  }
</style>
</head>
<body>
  <main class="page">
    <div class="profile-frame"></div>

    <header class="brand">
      <div class="brand-dot"></div>
      <div class="brand-name">Valtrenor</div>
    </header>

    <p class="profile-text">Valtrenor brings rare, exceptional wines to the Indonesian market. Wespecialize in French and Italian wines that even in Europe are very hard to get by. We have an extensive network of big and small, famous and lessknown winemakers that reserve a portion of their production for us. Together with them, we supply the market with an excellent range of the absolute best European wines. We buy our products directly at the winemaker in France or Italy Through a licensed importer, the wines are brought to Indonesia by airfreight and stored in air-conditioned, optimal conditions, awaiting distribution to our customers. All of this ensured that the wine loses none of its quality during transport from the winemaker to the customer. We always look out for partners that are eager to distribute or retail. Our intentions working with them are always to work on a long term basis. With these intentions we see that both sides together have to engage themselves to succeed in sales and establishing brand recognition in the Indonesian market. Our philosophy is based on trust, responsibility, mutual respect and of course a love for great wine! We advise our clients on tasting, food pairing, storing and aging the wine -and provide a technical datasheet with all our bottles. We pride ourselves in our customer service and are always available for any enquiry.</p>

    <svg class="glass-illustration" role="img" aria-label="Illustration of a large red wine glass, partly filled, cropped at the right edge" viewBox="0 0 287 866" preserveAspectRatio="none">
      <defs>
        <linearGradient id="glassTone" x1="0" y1="0" x2="0" y2="1">
          <stop offset="0" stop-color="#9a4a4c" stop-opacity="0.55"/>
          <stop offset="0.33" stop-color="#8a2226" stop-opacity="0.7"/>
          <stop offset="0.55" stop-color="#6e0508" stop-opacity="0.9"/>
          <stop offset="0.7" stop-color="#5a1214" stop-opacity="0.6"/>
          <stop offset="1" stop-color="#2a0a0b" stop-opacity="0.4"/>
        </linearGradient>
      </defs>
      <rect width="287" height="866" fill="url(#glassTone)"/>
    </svg>

    <footer class="contact-band">
      <span class="contact-email">info@valtrenor-example.eu</span>
    </footer>
  </main>
</body>
</html>
```